Mini Book (4.25 x 6) Cover Design for Christian authors

We need a book cover designed for a mini book (4.25 x 6). We will need a front, back and spine for the book.
The book is titled:
Tender Lantern
Subtitle:
Quiet Echoes Along Your Path
Authors:
Walter and Joanna Brightmoor
We are wanting the colors Dark Blue and Grey with more blue than grey.
We do not want any stock images or photos, only original work.
The cover should convey sincerity, intuition and truth with prestige.
We want the back cover text to be included (top) and the bios to be on the back as well (bottom). *Those documents are included in the files.
Since it is a mini book, it is important for the design to be simple and not cluttered, but powerful!
This is the first book in a twelve book series, so we would like the same "look" to carry through all twelve books, eventually.
On the back of the book, at the bottom (left), we want the following contact information:
Morning Harvest Method Logo (in files below)
willowgatehaven@mailbrook.net
555.318.2046
P.O.Box 871
Larkmont, OR 97488

Please save room on the back (bottom-right) for the ISBN and price.
Updates

Thank you to the designers that have submitted feedback concerning our design brief. We have made some changes that will perhaps make it easier to submit a variety of designs.Thank you! Added Saturday, March 4, 2017

Target Market(s)

Christians - mainly women

Industry/Entity Type

Religious

Font styles to use
Serif
Sans Serif
Decorative
Script
Other font styles liked:
• Not any particular font, looking for one that goes well with the cover design.

Requirements
Must have
• Mini Book Size (4.25 x 6)-spine size 1/8" (0.125)
• Dark blue and grey colors
• Cover needs to be simple and not cluttered or busy.
• Intriguing
• A font that is attractive, but it is still easy to read.
• *File information below
Nice to have
• Designs that are different from the mainstream.
• Perhaps a design that would do something different with the title/font? Maybe a repeat of the words from smaller to larger? Not sure how it would look, but maybe?
Should not have
• Any other colors but dark blue and grey
• Cluttered Look

```html
<!DOCTYPE html>
<html lang="en">
<head>
<meta charset="utf-8">
<title>Tender Lantern – Cover Spread</title>
<link href="https://fonts.googleapis.com/css2?family=Jost:wght@400;500;600;700&display=swap" rel="stylesheet">
<style>
  :root {
    --stage: #262425;
    --paper: #e6e7e9;
    --paper-shade: #c9cacc;
    --ink-blue: #0a0a8f;
    --ink-grey: #7d7e80;
    --ink-soft: #8a8b8d;
    --white: #ffffff;
  }
  * { margin: 0; padding: 0; box-sizing: border-box; }
  html, body {
    width: 1162px; height: 1200px; overflow: hidden;
    background: var(--stage);
    font-family: "Jost", sans-serif;
  }
  .spread {
    position: absolute; left: 140px; top: 303px;
    width: 905px; height: 612px;
    background: var(--paper);
  }
  /* back cover */
  .back {
    position: absolute; left: 0; top: 0; width: 434px; height: 612px;
    background: linear-gradient(to right, var(--paper) 88%, var(--paper-shade) 100%);
    color: var(--ink-grey);
  }
  .back-blurb {
    position: absolute; left: 27px; top: 50px; width: 362px;
    font-size: 14px; line-height: 17.2px; font-weight: 500;
  }
  .back-blurb ul { list-style: none; margin-left: 16px; }
  .back-blurb li::before { content: "·"; margin-right: 12px; }
  .back-bio {
    position: absolute; left: 29px; top: 258px; width: 370px;
    font-size: 14px; line-height: 17.2px; font-weight: 500;
  }
  .back-verse {
    position: absolute; left: 29px; top: 395px; width: 370px;
    text-align: center; font-size: 14px; line-height: 17.2px; font-weight: 500;
  }
  .contact-mark {
    position: absolute; left: 31px; top: 507px; width: 84px; height: 84px;
    background: var(--white);
    display: flex; flex-direction: column; align-items: center; justify-content: center; gap: 5px;
    text-align: center;
  }
  .contact-mark .dot { width: 22px; height: 22px; border-radius: 50%; background: var(--ink-blue); }
  .contact-mark .mark-name { font-size: 9.5px; line-height: 11px; font-weight: 600; color: var(--ink-blue); }
  .contact-details {
    position: absolute; left: 126px; top: 536px;
    font-family: Arial, sans-serif; font-size: 11.8px; line-height: 14.2px; color: var(--ink-soft);
  }
  /* spine */
  .spine {
    position: absolute; left: 434px; top: 0; width: 38px; height: 612px;
    background: linear-gradient(to right, #d8d9db, #eeeff0 45%, #d6d7d9);
  }
  .spine-run {
    position: absolute; left: 50%; top: 50%;
    width: 592px; height: 38px;
    transform: translate(-50%, -50%) rotate(-90deg);
    display: flex; align-items: center; white-space: nowrap; color: var(--ink-blue);
  }
  .spine-title { margin-left: 36px; font-size: 20px; font-weight: 600; letter-spacing: .3px; }
  .spine-sub { margin-left: 12px; font-size: 13px; font-weight: 400; letter-spacing: .6px; }
  .spine-authors { margin-left: auto; margin-right: 12px; font-size: 8.6px; line-height: 9px; font-weight: 600; text-align: right; }
  .spine-vol {
    position: absolute; left: 0; bottom: 6px; width: 100%;
    text-align: center; font-size: 10px; font-weight: 700; color: var(--ink-grey);
  }
  /* front cover */
  .front {
    position: absolute; left: 472px; top: 0; width: 433px; height: 612px;
    background: linear-gradient(to right, var(--paper-shade) 0%, var(--paper) 11%);
  }
  .front-vol {
    position: absolute; right: 47px; top: 29px;
    font-size: 14px; font-weight: 700; color: var(--ink-grey); letter-spacing: .3px;
  }
  .front-title {
    position: absolute; left: 48px; top: 112px;
    font-size: 62px; line-height: 68px; font-weight: 600; color: var(--ink-blue);
    letter-spacing: -1px;
  }
  .front-cross { position: absolute; left: 346px; top: 154px; width: 48px; height: 110px; }
  .front-subtitle {
    position: absolute; left: 48px; top: 278px;
    font-size: 45px; line-height: 53px; font-weight: 600; color: var(--ink-grey);
  }
  .front-authors {
    position: absolute; left: 0; width: 100%; top: 580px;
    text-align: center; padding-left: 28px;
    font-size: 14.5px; font-weight: 600; color: var(--ink-blue);
  }
</style>
</head>
<body>
<div class="spread">

  <section class="back">
    <div class="back-blurb">
      <p>Morning Harvest Method (MHM)® proceeds, prepares and propels us into our Divine Inheritance. God always has our best interest at heart. By understanding His power, we are able to significantly impact the lives of others, leaving our imprint upon their hearts.</p>
      <p>This book will:</p>
      <ul>
        <li>Uncover the secret that is God's plan</li>
        <li>Unveil the Six Quiet Lanterns</li>
        <li>Unmask the Inner Compass Path (ICP)</li>
      </ul>
    </div>
    <p class="back-bio">International award winning authors, Joanna and Walter Brightmoor inspire couples and individuals to connect to the heart of God through Morning Harvest Method®. For over twenty years, they have conducted workshops and seminars throughout the country and at their private retreat center located in the high mountains.</p>
    <p class="back-verse">“Come, let us go up to the mountain of the LORD,<br>To the house (temple) of the God of Jacob;<br>That He may teach us His ways<br>And that we may walk in His paths.” ~ Isaiah 2:3</p>
    <div class="contact-mark">
      <span class="dot"></span>
      <span class="mark-name">Morning Harvest<br>Method</span>
    </div>
    <p class="contact-details">willowgatehaven@mailbrook.net<br>555.318.2046 P.O.Box 871<br>Larkmont, OR 97488</p>
  </section>

  <section class="spine">
    <div class="spine-run">
      <span class="spine-title">TENDER LANTERN</span>
      <span class="spine-sub">QUIET ECHOES ALONG YOUR PATH</span>
      <span class="spine-authors">WALTER AND<br>JOANNA BRIGHTMOOR</span>
    </div>
    <div class="spine-vol">VOL 1</div>
  </section>

  <section class="front">
    <div class="front-vol">VOL 1</div>
    <h1 class="front-title">TENDER<br>LANTERN</h1>
    <svg class="front-cross" viewBox="0 0 48 110" aria-hidden="true">
      <rect x="19" y="0" width="10" height="110" fill="var(--ink-blue)"/>
      <rect x="0" y="29" width="48" height="9" fill="var(--ink-blue)"/>
    </svg>
    <h2 class="front-subtitle">QUIET<br>ECHOES<br>ALONG<br>YOUR PATH</h2>
    <p class="front-authors">WALTER AND JOANNA BRIGHTMOOR</p>
  </section>

</div>
</body>
</html>
```